Business card design needed

After a business card which portrays the same precision tig welding and performance fabrications we offer customers. Catering mainly for the automotive market, but process work for marine, industrial & hospitality work is definitely welcome.

We provide the same level quality, care and workmanship regardless of how big or small the job is. Quality is the first and foremost for customers looking for the highest standards around along with a customised look not found anywhere else.

Our offering is tailor made for each customer and where needed, a completely individual look

Colours - red, black and white (as per the attached logo)

The design should portray a customised/one-off solution for each customer with a high attention to detail.
Updates

The brief should have included this design is required for a 2 sided card

Industry/Entity Type

Hospitality

Contact Information for Business Card

Blue Anchor Metalworks
3/14 Corwen Hale Avenue
North Wollongong NSW 2500

Ph: 02 4871 3064
Mob: 0412 586 137
Email: blueanchormetalworks@mailhaven.example
Facebook: www.socialpage.example/blueanchormetalworks

Requirements
Must have
• Must have a catchy front side without being cluttered & brief but list off main offerings on the back. For eg
- customised concept & design for each project
- 2D & 3D modelling & machining
- catering for single or mass prodcued items

```html
<!DOCTYPE html>
<html lang="en">
<head>
<meta charset="utf-8">
<title>Blue Anchor Metalworks – Business Card</title>
<link rel="stylesheet" href="https://fonts.googleapis.com/css2?family=Montserrat:ital,wght@0,400;0,500;0,700;1,400&display=swap">
<style>
  :root {
    --page: #f2f2f2;
    --card-white: #ffffff;
    --card-black: #050607;
    --ink: #111111;
    --ink-soft: #1c1c1c;
    --white: #ffffff;
    --red: #e41e26;
    --red-deep: #9c1520;
    --band-dark: #0c0c0c;
    --band-light: #4a4a4a;
  }
  html, body {
    margin: 0;
    padding: 0;
    width: 1200px;
    height: 1000px;
    overflow: hidden;
    background: radial-gradient(ellipse at center, #ffffff 0%, var(--page) 75%);
    font-family: "Montserrat", Arial, sans-serif;
  }
  .card {
    position: absolute;
    left: 291px;
    width: 617px;
    height: 347px;
    overflow: hidden;
    box-shadow: 0 3px 8px rgba(0,0,0,0.22);
  }
  .card--front { top: 125px; background: var(--card-white); color: var(--ink); }
  .card--back {
    top: 533px;
    background:
      radial-gradient(ellipse 260px 200px at 520px 330px, rgba(90,90,90,0.75) 0%, rgba(5,6,7,0) 100%),
      var(--card-black);
    color: var(--white);
  }
  .accent-panel {
    position: absolute;
    right: 0;
    top: 0;
    width: 130px;
    height: 270px;
  }
  .wordmark {
    position: absolute;
    display: flex;
    align-items: center;
    gap: 10px;
    font-weight: 700;
    letter-spacing: -0.3px;
    white-space: nowrap;
  }
  .wordmark__dot {
    width: 14px;
    height: 14px;
    background: var(--red);
    flex: none;
  }
  .card--front .wordmark { left: 34px; top: 62px; font-size: 25px; color: var(--ink); }
  .card--back .wordmark { left: 48px; top: 97px; font-size: 31px; color: var(--white); }
  .wordmark-phone {
    position: absolute;
    left: 35px;
    top: 101px;
    font-size: 15px;
    font-weight: 700;
    letter-spacing: 5px;
    color: var(--ink);
    border-top: 2px solid var(--ink);
    padding-top: 5px;
  }
  .name-band {
    position: absolute;
    left: 0;
    top: 163px;
    width: 464px;
    height: 41px;
    background: linear-gradient(90deg, var(--band-dark) 0%, var(--band-dark) 55%, var(--band-light) 100%);
    clip-path: polygon(0 0, 100% 0, 95.5% 100%, 0 100%);
    display: flex;
    align-items: center;
    padding-left: 34px;
    box-sizing: border-box;
    font-size: 17px;
    color: var(--white);
  }
  .name-band__name { font-weight: 700; }
  .marker {
    display: inline-block;
    width: 8px;
    height: 8px;
    background: var(--red);
    margin: 0 8px;
    vertical-align: middle;
  }
  .name-band__role { font-style: italic; }
  .address {
    position: absolute;
    left: 34px;
    top: 244px;
    font-size: 15px;
    line-height: 21.5px;
    color: var(--ink-soft);
  }
  .address__company { font-weight: 700; }
  .contact {
    position: absolute;
    left: 246px;
    top: 244px;
    font-size: 15px;
    line-height: 21.5px;
    color: var(--ink-soft);
    border-collapse: collapse;
  }
  .contact td { padding: 0; vertical-align: baseline; }
  .contact__label { font-weight: 700; width: 34px; }
  .contact__email { font-size: 13px; }
  .offerings {
    position: absolute;
    left: 38px;
    top: 210px;
    margin: 0;
    padding: 0;
    list-style: none;
    font-size: 15px;
    line-height: 22.6px;
  }
  .offerings li { display: flex; align-items: center; }
  .offerings .marker { margin: 0 6px 0 0; }
</style>
</head>
<body>

<section class="card card--front" aria-label="Business card front">
  <svg class="accent-panel" viewBox="0 0 130 270" aria-hidden="true">
    <defs>
      <linearGradient id="accentFront" x1="0" y1="0" x2="0.4" y2="1">
        <stop offset="0" stop-color="#ee1f27"/>
        <stop offset="1" stop-color="#9c1520"/>
      </linearGradient>
    </defs>
    <polygon points="40,0 130,0 130,226 0,270" fill="url(#accentFront)"/>
  </svg>

  <div class="wordmark"><span class="wordmark__dot"></span>Blue Anchor Metalworks</div>
  <div class="wordmark-phone">0412 586 137</div>

  <div class="name-band">
    <span class="name-band__name">Marlo Keswin</span>
    <span class="marker"></span>
    <span class="name-band__role">Director</span>
  </div>

  <div class="address">
    <div class="address__company">Blue Anchor Metalworks</div>
    <div>3/14 Corwen Hale Avenue</div>
    <div>North Wollongong</div>
    <div>NSW 2500</div>
  </div>

  <table class="contact">
    <tr><td class="contact__label">P</td><td><b>:</b> 02 4871 3064</td></tr>
    <tr><td class="contact__label">M</td><td><b>:</b> 0412 586 137</td></tr>
    <tr><td class="contact__label">E</td><td><b>:</b> <span class="contact__email">blueanchormetalworks@mailhaven.example</span></td></tr>
    <tr><td class="contact__label">FB</td><td><b>:</b> blueanchormetalworks</td></tr>
  </table>
</section>

<section class="card card--back" aria-label="Business card back">
  <svg class="accent-panel" viewBox="0 0 130 270" aria-hidden="true">
    <defs>
      <linearGradient id="accentBack" x1="0" y1="0" x2="0.4" y2="1">
        <stop offset="0" stop-color="#ee1f27"/>
        <stop offset="1" stop-color="#9c1520"/>
      </linearGradient>
    </defs>
    <polygon points="40,0 130,0 130,226 0,270" fill="url(#accentBack)"/>
  </svg>

  <div class="wordmark"><span class="wordmark__dot"></span>Blue Anchor Metalworks</div>

  <ul class="offerings">
    <li><span class="marker"></span>Precision tig welding of all materials</li>
    <li><span class="marker"></span>Customised concept &amp; design for each project</li>
    <li><span class="marker"></span>2D &amp; 3D modelling and machining</li>
    <li><span class="marker"></span>Catering for one-off &amp; production work</li>
    <li><span class="marker"></span>Fully equipped fabrication workshop</li>
  </ul>
</section>

</body>
</html>
```